Dermatopathology Brochure

We need a brochure that will let potential clients know our services. It needs to be clean, clear, and eye-catching. A modern feel is what we would like. Some previous work done for us in the past has been included. We have uploaded a word file with content as well. You may also use information from our website, skinslidecrest.com. You don't have to use all available information, but the content of the word file is our main message.
Updates

Although the postcard highlights our MeetPlume based online clinicopathologic correlation, we would like our brochure to be more general. In other words, we use postcards to make a single important point, but the brochure should be more balanced regarding our services. Also, the postcard was great for us, but we don't necessarily want to repeat its look exactly. We liked the postacard's clean and balanced look. We would like to try having our brochure more "friendly" and conversational, yet professional. Thanks!

Target Market(s)

Physicians, mostly dermatologists.

Industry/Entity Type

Work

```html
<!DOCTYPE html>
<html lang="en">
<head>
<meta charset="utf-8">
<title>Clearfield Dermatology &amp; Dermatopathology – Brochure</title>
<link rel="stylesheet" href="https://fonts.googleapis.com/css2?family=Open+Sans:wght@400;600;700&family=Fira+Sans:wght@700&display=swap">
<style>
  :root {
    --ink: #231f1e;
    --red: #e3242b;
    --dark: #2f2927;
    --white: #ffffff;
    --blush: #f1c9cf;
    --rose: #e3a0aa;
    --tissue-1: #d98a96;
    --tissue-2: #f0c3c8;
  }
  * { box-sizing: border-box; margin: 0; padding: 0; }
  html, body { width: 1200px; height: 849px; overflow: hidden; background: var(--white); }
  body { font-family: "Open Sans", Arial, sans-serif; color: var(--ink); }

  .brochure { position: relative; width: 1200px; height: 849px; overflow: hidden; }

  .inside-top {
    position: absolute; left: 0; top: 0; width: 1200px; height: 468px;
    background: linear-gradient(180deg, var(--white) 0%, var(--white) 58%, #f7e3e6 70%, var(--blush) 85%, var(--rose) 100%);
  }
  .rule-band { position: absolute; left: 0; top: 468px; width: 1200px; height: 10px; background: var(--red); }
  .cover-band { position: absolute; left: 0; top: 478px; width: 1200px; height: 330px; background: var(--dark); }
  .tissue-strip {
    position: absolute; left: 0; top: 808px; width: 1200px; height: 41px;
    background: linear-gradient(90deg, var(--tissue-1), var(--tissue-2) 30%, var(--tissue-1) 55%, var(--tissue-2) 80%, var(--tissue-1));
  }
  .fold { position: absolute; top: 0; width: 1px; height: 808px; background: rgba(0,0,0,0.06); }

  .welcome-card {
    position: absolute; left: 40px; top: 0; width: 318px; height: 428px;
    background: var(--white); border-radius: 0 0 26px 26px;
    padding: 38px 18px 0; text-align: center;
    font-size: 17px; line-height: 22px;
  }

  .portrait {
    position: absolute; left: 478px; top: 0; width: 240px; height: 163px;
    background: linear-gradient(180deg, #d9c9a8 0%, #b8a784 55%, #2d3344 100%);
  }
  .bio {
    position: absolute; left: 445px; top: 187px; width: 310px;
    text-align: center; font-size: 17px; line-height: 22px;
  }

  .instrument-art {
    position: absolute; left: 800px; top: 0; width: 400px; height: 160px;
    background: linear-gradient(180deg, #eeeeee 0%, #d4d4d4 50%, #f4f4f4 100%);
  }
  .headline {
    position: absolute; left: 860px; top: 182px; width: 280px;
    font-family: "Fira Sans", "Open Sans", sans-serif; font-weight: 700;
    font-size: 32px; line-height: 35px; text-align: center; color: var(--ink);
  }
  .tagline {
    position: absolute; left: 870px; top: 363px; width: 260px;
    font-weight: 700; font-size: 20px; line-height: 23px; text-align: center; color: var(--red);
  }

  .cover-title {
    position: absolute; left: 0; width: 400px; text-align: center;
    font-weight: 700; font-size: 29px; color: var(--red); letter-spacing: 0.4px;
  }
  .cover-title.first { top: 559px; }
  .cover-title.second { top: 689px; }

  .contact {
    position: absolute; left: 430px; top: 542px; width: 340px;
    text-align: center; color: var(--red); font-size: 17px; line-height: 25px;
  }
  .contact dt { font-weight: 700; }
  .contact dd { margin-bottom: 25px; }
  .contact .web { font-weight: 700; }

  .brand-name {
    position: absolute; left: 800px; top: 697px; width: 400px;
    font-size: 16px; font-weight: 400; color: var(--white);
    text-align: center; line-height: 24px;
  }
  .brand-name .line-wide { letter-spacing: 9px; }
</style>
</head>
<body>
<main class="brochure">
  <div class="inside-top"></div>
  <div class="rule-band"></div>
  <div class="cover-band"></div>
  <div class="tissue-strip" role="img" aria-label="Stained skin tissue micrograph strip in pink tones"></div>
  <div class="fold" style="left:400px"></div>
  <div class="fold" style="left:800px"></div>

  <section class="welcome-card">
    <p>We know how important reliable dermatopathology services are to your patients and your practice. As your partner in patient care, we want to do our part in helping you arrive at the diagnosis for each patient you entrust to us. We also know that part of our job is making working with us as smooth as possible. We can provide courier pick up service to local practices, and we will help arrange overnight delivery for specimens sent from outside our area. We'll handle the details so you can focus on the care of your patients.</p>
  </section>

  <section>
    <div class="portrait" role="img" aria-label="Portrait photograph of Dr. Hale"></div>
    <p class="bio">Dr. Hale graduated from Northbrook Medical College and completed his Internal Medicine internship at the Valley Crest Medical program. He completed his Dermatology residency, and subsequently his Dermatopathology Fellowship, at Ashgrove College of Medicine in Fairhaven. Dr. Hale is board-certified in Dermatology and Dermatopathology.</p>
  </section>

  <section>
    <div class="instrument-art" role="img" aria-label="Close-up photograph of microscope objective lenses"></div>
    <h1 class="headline">MeetPlume-based, online clinico - pathologic correlation</h1>
    <p class="tagline">LIKE HAVING A DERMATOPATHOLOGIST IN YOUR OFFICE</p>
  </section>

  <h2 class="cover-title first">THE DIAGNOSIS</h2>
  <h2 class="cover-title second">IN FOCUS</h2>

  <dl class="contact">
    <dt>Mailing address</dt>
    <dd>4172 W. Marlow Ave. #214, Fairhaven, CA 90512</dd>
    <dt>Telephone</dt>
    <dd>800.555.0142</dd>
    <dt class="web">www.skinslidecrest.com</dt>
  </dl>

  <p class="brand-name"><span class="line-wide">CLEARFIELD</span><br>DERMATOLOGY &amp; DERMATOPATHOLOGY</p>
</main>
</body>
</html>
```